nutrition company business card

I would like to have a business card that has two sides, one being the green color from the Company name on the logo. I am open to ideas and looks that work with my logo. I like the idea of having a negative image of the tree on the green side.

For my information on the card I must have:
Linda Moorcombe
415-872-6041
lindamoorcombe@quellmail.net

This area will need to be updated once I complete my schooling.

Reason: I need to extend my deadline by one day as I have been sick the last week and not had time to review all the new designs. Thank you.

Industry/Entity Type

Nutrition

Requirements
Must have
• I would like to have a business card that has two sides, one being the green color from the Company name on the logo. I am open to ideas and looks that work with my logo. I like the idea of having a negative image of the tree on the green side.
• For my information on the card I must have:
• Linda Moorcombe
• 415-872-6041
• lindamoorcombe@quellmail.net
• This area will need to be updated once I complete my schooling.

```html
<!DOCTYPE html>
<html lang="en">
<head>
<meta charset="utf-8">
<title>Rootwell Nutrition – Business Card</title>
<link rel="stylesheet" href="https://fonts.googleapis.com/css2?family=Arimo:wght@400;700&display=swap">
<style>
  :root {
    --paper: #ffffff;
    --bark: #9a8172;
    --leaf: #6cc21c;
    --leaf-light: #84d42a;
    --leaf-deep: #5aa813;
    --band-shade: rgba(20, 70, 0, 0.32);
    --ink-light: #ffffff;
  }
  * { margin: 0; padding: 0; box-sizing: border-box; }
  html, body {
    width: 1200px;
    height: 686px;
    overflow: hidden;
    background: var(--paper);
  }
  .card {
    position: relative;
    width: 1200px;
    height: 686px;
    display: flex;
    font-family: "Arimo", Arial, sans-serif;
  }
  .brand-side {
    position: relative;
    width: 686px;
    height: 686px;
    background: var(--paper);
  }
  .brand-ring {
    position: absolute;
    inset: 0;
  }
  .brand-name {
    position: absolute;
    inset: 0;
    display: flex;
    align-items: center;
    justify-content: center;
    text-align: center;
    font-weight: 700;
    font-size: 46px;
    line-height: 1.2;
    color: var(--bark);
  }
  .contact-side {
    position: relative;
    width: 514px;
    height: 686px;
    background:
      radial-gradient(ellipse at 70% 20%, var(--leaf-light) 0%, transparent 60%),
      radial-gradient(ellipse at 20% 85%, var(--leaf-light) 0%, transparent 55%),
      linear-gradient(160deg, var(--leaf) 0%, var(--leaf-deep) 100%);
  }
  .band {
    position: absolute;
    left: 0;
    width: 100%;
    display: flex;
    align-items: center;
    justify-content: center;
    color: var(--ink-light);
    font-size: 30px;
  }
  .band--shade { background: var(--band-shade); }
  .band--top    { top: 0;     height: 114px; }
  .band--name   { top: 114px; height: 109px; font-weight: 700; }
  .band--role   { top: 223px; height: 118px; }
  .band--phone  { top: 341px; height: 111px; }
  .band--email  { top: 452px; height: 117px; }
  .band--bottom { top: 569px; height: 117px; }
</style>
</head>
<body>
  <main class="card">
    <section class="brand-side">
      <svg class="brand-ring" width="686" height="686" viewBox="0 0 686 686" aria-hidden="true">
        <circle cx="343" cy="343" r="283" fill="none" stroke="var(--bark)" stroke-width="14"/>
      </svg>
      <div class="brand-name">Rootwell<br>Nutrition</div>
    </section>

    <section class="contact-side" role="img" aria-label="Green crinkled paper texture background">
      <div class="band band--top band--shade"></div>
      <div class="band band--name">Linda Moorcombe</div>
      <div class="band band--role band--shade">Owner</div>
      <div class="band band--phone">415-872-6041</div>
      <div class="band band--email band--shade">lindamoorcombe@quellmail.net</div>
      <div class="band band--bottom"></div>
    </section>
  </main>
</body>
</html>
```